Einladungskarten-Design für Reinigung & Gebäudemangement
Zielgruppe:
Potentielle Kunden/Entscheider Einrichtungsleiter, Geschäftführer für den Bereich Alten- und Pflegeheime, Krankenhäuser.
Das Angebot geht über Verpflegungslösung, Reinigung, Gebäudemangement und Innovationen (z.B. zum Thema Digitalisierung, Roboting, .....).
Der Claim des Unternehmens ist 'Quality of Life Services = Services der Lebensqualität'
Aufgabenstellung
Gerne Pop-Up oder auch Relief - hochwertige Haptik von Umschlag und Karte ggf. Sonderformat d.h. nicht Standard DL quer
Sollte aber dennoch klassich gut wirken.
Die persönliche Note erhält die Karte durch handschriftliche Personalisierung durch den Sales Mitarbeiter.
Die Karte soll folgenden Text enthalten.
Text:
Das neue Jahr liegt vor Ihnen.
Nutzen Sie seine Chancen und ergreifen Sie seine Möglichkeiten.
Beispielsweise mit einem Gespräch
über inspierierende Ideen und neue Konzepte zur Steigerung der Lebensqualität
in Ihrem Hause.
Wir freuen uns mit Ihnen in Kontakt zu sein.
Der Umschlag soll Absenderadresse und Logo enthalten - dies wird nach Prämierung bekannt gegeben.
Natürlich kann auf der Rückseite der Karte auch das Logo mit Claim aufgedruckt werden.
Alle Bildrechte sollen nach Prämierung auf den Auftraggeber übergehen.

```html
<!DOCTYPE html>
<html lang="de">
<head>
<meta charset="utf-8">
<title>Neujahrskarte 2018</title>
<link rel="stylesheet" href="https://fonts.googleapis.com/css2?family=Lato:wght@300;700&family=Rubik:wght@300&display=swap">
<style>
  :root {
    --sky-blue: #7f9cb8;
    --sky-dusk: #3f5c78;
    --sky-pale: #f4ede6;
    --sky-rose: #e3d3d8;
    --valley-dark: #17212e;
    --valley-mist: #c9ccd6;
    --ink: #2a2a2a;
    --white: #ffffff;
  }
  html, body {
    margin: 0;
    padding: 0;
    width: 800px;
    height: 1200px;
    overflow: hidden;
    background: var(--white);
  }
  .card {
    position: relative;
    width: 800px;
    height: 1200px;
    overflow: hidden;
    font-family: "Lato", sans-serif;
  }
  .panel {
    position: absolute;
    left: 0;
    width: 800px;
    height: 600px;
  }
  .panel--back {
    top: 0;
    background:
      radial-gradient(ellipse 70% 18% at 70% 14%, rgba(63,92,120,0.75), transparent 70%),
      radial-gradient(ellipse 45% 25% at 95% 40%, rgba(127,156,184,0.7), transparent 70%),
      radial-gradient(ellipse 60% 15% at 10% 25%, rgba(127,156,184,0.55), transparent 70%),
      radial-gradient(ellipse 55% 20% at 50% 85%, rgba(227,211,216,0.9), transparent 70%),
      linear-gradient(180deg, #b9c6d4 0%, var(--sky-rose) 35%, var(--sky-pale) 60%, #e9e2e4 100%);
  }
  .panel--front {
    top: 600px;
    background:
      radial-gradient(ellipse 55% 12% at 50% 50%, rgba(244,237,230,0.9), transparent 70%),
      radial-gradient(ellipse 70% 10% at 60% 70%, rgba(201,204,214,0.75), transparent 70%),
      linear-gradient(180deg, #aebccb 0%, var(--sky-pale) 25%, var(--sky-rose) 42%, #6f8aa3 54%, #4d6580 66%, #2c3b4d 80%, var(--valley-dark) 100%);
  }
  .brand {
    position: absolute;
    left: 60px;
    top: 64px;
    margin: 0;
    transform: rotate(180deg);
    color: var(--ink);
    font-weight: 700;
    font-size: 24px;
    line-height: 1;
  }
  .greeting {
    position: absolute;
    left: 64px;
    top: 928px;
    color: var(--white);
  }
  .greeting__year {
    margin: 0;
    font-family: "Rubik", sans-serif;
    font-weight: 300;
    font-size: 88px;
    line-height: 1;
    letter-spacing: 1px;
    color: transparent;
    -webkit-text-stroke: 1.6px var(--white);
  }
  .greeting__line {
    margin: 18px 0 0 1px;
    font-weight: 300;
    font-size: 24px;
    letter-spacing: 0.2px;
  }
</style>
</head>
<body>
  <main class="card">
    <section class="panel panel--back" role="img" aria-label="Weicher Himmel in Blau, Rosa und Creme, Rückseite der Faltkarte">
      <p class="brand">lumeva</p>
    </section>
    <section class="panel panel--front" role="img" aria-label="Wanderer mit Hut blickt bei Morgendämmerung über ein nebelverhangenes Bergtal">
    </section>
    <div class="greeting">
      <h1 class="greeting__year">2018</h1>
      <p class="greeting__line">Ein neues Jahr erwartet Sie...</p>
    </div>
  </main>
</body>
</html>
```